Candle company needs a label for candle

Looking for a designer to create my candle label. I am going to attach a few pictures of my vision for the label as well as my Company Logo and jar I have puchased. I'm going for the modern rustic feel but you are the designer and have full trust in your abilities. The label is going to be printed on Kraft paper (2x3) so looking for the font to be black. The candle label MUST include the following information:
Candle Birchway Co.
NO. 01: Eucalyptus + Spearmint
Handmade In NJ
Soy Wax
9oz

Industry/Entity Type

Candle Industry

Colors

Designer to choose colors to be used in the design.

Requirements
Should not have
• Any images

```html
<!DOCTYPE html>
<html lang="en">
<head>
<meta charset="utf-8">
<title>Candle Birchway Co. — Label No. 01</title>
<link rel="stylesheet" href="https://fonts.googleapis.com/css2?family=Archivo:wght@400;500;700&display=swap">
<style>
  :root {
    --page: #ffffff;
    --kraft: #c99c6b;
    --kraft-deep: #bb8d5d;
    --ink: #23272c;
    --shadow: rgba(0, 0, 0, 0.35);
  }
  * { margin: 0; padding: 0; box-sizing: border-box; }
  html, body {
    width: 826px;
    height: 1200px;
    overflow: hidden;
    background: var(--page);
  }
  .canvas {
    position: relative;
    width: 826px;
    height: 1200px;
  }
  .label {
    position: absolute;
    left: 43px;
    top: 353px;
    width: 740px;
    height: 494px;
    box-shadow: 6px 8px 10px var(--shadow);
    font-family: "Archivo", Arial, sans-serif;
    color: var(--ink);
    overflow: hidden;
  }
  .label__pattern {
    position: absolute;
    inset: 0;
    background: radial-gradient(ellipse at 50% 45%, var(--kraft) 0%, var(--kraft) 55%, var(--kraft-deep) 100%);
  }
  .brand-mark {
    position: absolute;
    left: 0;
    right: 0;
    top: 96px;
    display: flex;
    justify-content: center;
    align-items: center;
    gap: 12px;
    font-weight: 400;
    font-size: 24px;
    letter-spacing: 4px;
    text-transform: uppercase;
  }
  .brand-mark__square {
    width: 14px;
    height: 14px;
    border: 1.5px solid var(--ink);
  }
  .label__title {
    position: absolute;
    left: 0;
    right: 0;
    top: 228px;
    text-align: center;
    font-weight: 700;
    font-size: 42px;
    letter-spacing: 1px;
    line-height: 1;
  }
  .label__scent {
    position: absolute;
    left: 50%;
    top: 290px;
    transform: translateX(-50%);
    padding: 7px 16px 6px;
    border: 1.5px solid var(--ink);
    font-weight: 500;
    font-size: 19px;
    letter-spacing: 0.5px;
    white-space: nowrap;
  }
  .details {
    position: absolute;
    left: 166px;
    width: 410px;
    top: 376px;
    height: 51px;
  }
  .details__rule {
    position: absolute;
    left: 0;
    right: 0;
    border-top: 2px dotted var(--ink);
  }
  .details__rule--top { top: 0; }
  .details__rule--bottom { bottom: 0; }
  .details__divider {
    position: absolute;
    left: 50%;
    top: 12px;
    bottom: 12px;
    border-left: 2px dotted var(--ink);
  }
  .details__item {
    position: absolute;
    top: 17px;
    font-size: 16px;
    font-weight: 400;
    letter-spacing: 0.6px;
    word-spacing: 4px;
    text-transform: uppercase;
  }
  .details__item--origin { left: 15px; }
  .details__item--wax { left: 255px; }
  .label__weight {
    position: absolute;
    left: 0;
    right: 0;
    top: 449px;
    text-align: center;
    font-size: 14px;
    font-weight: 700;
  }
</style>
</head>
<body>
  <main class="canvas">
    <section class="label">
      <div class="label__pattern" role="img" aria-label="Faint swirling floral pattern printed across kraft paper"></div>

      <div class="brand-mark">
        <span class="brand-mark__square"></span>
        <span class="brand-mark__name">Candle Birchway Co.</span>
      </div>

      <h1 class="label__title">CANDLE BIRCHWAY CO</h1>
      <p class="label__scent">NO. 01: EUCALYPTUS + SPEARMINT</p>

      <div class="details">
        <span class="details__rule details__rule--top"></span>
        <span class="details__item details__item--origin">Handmade in NJ</span>
        <span class="details__divider"></span>
        <span class="details__item details__item--wax">Soy wax</span>
        <span class="details__rule details__rule--bottom"></span>
      </div>

      <p class="label__weight">9OZ</p>
    </section>
  </main>
</body>
</html>
```